Landing Page for a new, High Production, farming technology

Brightfield Yield
We need a single landing page, with an email signup for more information.
We build self-contained, farming boxes out of ISO containers. These containers use hydroponics and LED lighting to provide a year round growing environment for crops. So, you could grow crops anywhere at any time of the year in any environment.
For the purpose of this site, we will be doing split testing between several different themes using different sites and keywords.
This site's focus should be providing our product to people searching for high production farming technology.
We'll be focusing on the following key words: Agriculture, aquaponics, farm, garden, hydroponics, organic food, subsistence farming, urban farming, vertical garden.
Target Market(s)
We are going to be using this page to judge that
Number of Pages Required
1 page
Look and feel
Each slider illustrates characteristics of the customer's brand and the style your logo design should communicate.

```html
<!DOCTYPE html>
<html lang="en">
<head>
<meta charset="utf-8">
<title>Brightfield Yield</title>
<link href="https://fonts.googleapis.com/css2?family=Montserrat:wght@400;500;600&family=Open+Sans:ital,wght@0,400;0,700;1,600&display=swap" rel="stylesheet">
<style>
  :root {
    --orange: #e8964f;
    --green: #9ab87f;
    --ink: #1c1c1c;
    --white: #ffffff;
    --footer: #020b0c;
    --hero-deep: #123f5c;
    --hero-mid: #3e86a8;
    --hero-light: #8fc3d6;
    --leaf: #5fbf3a;
  }
  * { margin: 0; padding: 0; box-sizing: border-box; }
  html, body { width: 1200px; height: 780px; overflow: hidden; }
  body { font-family: "Open Sans", sans-serif; background: var(--white); position: relative; }

  .site-header {
    position: absolute; left: 0; top: 0; width: 1200px; height: 104px;
    background: var(--white); border-bottom: 6px solid var(--orange);
  }
  .brand {
    position: absolute; left: 100px; top: 30px;
    display: flex; align-items: center; gap: 12px;
    font-family: "Montserrat", sans-serif; font-weight: 500;
    font-size: 24px; letter-spacing: 3px; color: var(--green);
  }
  .brand-mark { width: 30px; height: 30px; background: var(--orange); }
  .main-nav {
    position: absolute; right: 98px; top: 41px;
    display: flex; align-items: center; gap: 30px;
    font-family: "Montserrat", sans-serif; font-weight: 600; font-size: 15.5px;
    color: var(--ink); letter-spacing: 0.2px;
  }
  .main-nav .active { color: var(--orange); }
  .main-nav svg { display: block; }

  .hero {
    position: absolute; left: 0; top: 104px; width: 1200px; height: 597px;
    background:
      radial-gradient(ellipse 320px 260px at 870px 300px, rgba(95,191,58,0.55), transparent 70%),
      radial-gradient(ellipse 260px 200px at 1150px 260px, rgba(95,191,58,0.4), transparent 70%),
      linear-gradient(90deg, var(--hero-light) 0%, var(--hero-mid) 35%, var(--hero-deep) 55%, var(--hero-mid) 80%, var(--hero-light) 100%);
  }
  .hero-content { position: absolute; left: 92px; top: 150px; color: var(--white); }
  .hero-title { font-family: "Montserrat", sans-serif; font-weight: 500; line-height: 1; }
  .hero-title .line-1 { display: block; font-size: 51px; }
  .hero-title .line-2 { display: block; font-size: 81px; margin-top: 4px; }
  .tagline {
    margin-top: 30px; margin-left: 8px;
    font-style: italic; font-weight: 600; font-size: 22px;
    text-shadow: 0 1px 3px rgba(0,0,0,0.3);
  }
  .signup {
    position: absolute; left: 99px; top: 365px; display: flex; height: 64px;
  }
  .signup input {
    width: 545px; height: 64px; border: 0; padding: 0 27px;
    font-family: "Open Sans", sans-serif; font-size: 17px; color: var(--ink);
    background: var(--white); outline: none;
  }
  .signup input::placeholder { color: #444; }
  .signup button {
    width: 147px; height: 64px; border: 0; background: var(--green);
    color: var(--white); font-family: "Open Sans", sans-serif; font-weight: 700;
    font-size: 17px; letter-spacing: 0.5px;
  }
  .slider-dots {
    position: absolute; left: 563px; top: 502px; display: flex; gap: 5px;
  }
  .slider-dots span {
    width: 14px; height: 14px; border-radius: 50%; border: 2px solid var(--white);
  }
  .slider-dots .current { background: var(--white); }

  .site-footer {
    position: absolute; left: 0; top: 701px; width: 1200px; height: 79px;
    background: var(--footer); color: var(--white);
    display: flex; align-items: center; justify-content: center;
    font-size: 13px;
  }
</style>
</head>
<body>
  <header class="site-header">
    <div class="brand"><span class="brand-mark"></span>BRIGHTFIELD YIELD</div>
    <nav class="main-nav">
      <span class="active">HOME</span>
      <span>ABOUT US</span>
      <span>SERVICES</span>
      <span>WHY US</span>
      <span>BLOG</span>
      <span>CONTACT US</span>
      <svg width="16" height="16" viewBox="0 0 16 16" aria-label="Search">
        <circle cx="6.5" cy="6.5" r="4.8" fill="none" stroke="#1c1c1c" stroke-width="2.4"/>
        <line x1="10" y1="10" x2="14.5" y2="14.5" stroke="#1c1c1c" stroke-width="2.8" stroke-linecap="round"/>
      </svg>
    </nav>
  </header>

  <section class="hero" role="img" aria-label="Photo of a container farm interior with rows of racks, LED lights and leafy greens">
    <div class="hero-content">
      <h1 class="hero-title"><span class="line-1">BRIGHTFIELD</span><span class="line-2">YIELD</span></h1>
      <p class="tagline">We build self-contained, farming boxes out of ISO containers.</p>
    </div>
    <form class="signup">
      <input type="email" placeholder="Email Address">
      <button type="button">SIGN UP</button>
    </form>
    <div class="slider-dots"><span class="current"></span><span></span><span></span><span></span></div>
  </section>

  <footer class="site-footer">Copyrights © 2018, Brightfield Yield. All Rights Reserved.</footer>
</body>
</html>
```